Visitenkarten-Design für ein Beratungsunternehmen im Immobilienbereich
Zielgruppe
Wir sind ein Beratungsunternehmen im Immobilienbereich. Von der Planung, Ingenieuring, bis hin zum Vertriebskonzept
Aufgabenstellung
Das vorhandene Logo mit den zugehörigen Farben und Schriften
Firmennamen: FORLAN
Name: Jörg Tannhuber
Geschäftsführer
Anschrift: Lindenhofweg 14, 64683 Einhausen
What3word: ///kiesel.wolken.taschen
Telefon: +49 6251 4710562
Mobil: +49 162 5074831
Mail: kontakt@forlan-beispiel.immo
Web: www.forlan-beispiel.immo
Slogan: Für Ihren MehrWert
Das Logo soll als Prägung und teilweise in silber/ heissfolie ausgeführt werden.

```html
<!DOCTYPE html>
<html lang="de">
<head>
<meta charset="utf-8">
<title>FORLAN – Visitenkarte</title>
<link rel="stylesheet" href="https://fonts.googleapis.com/css2?family=Poppins:wght@300;400;500&display=swap">
<style>
  :root {
    --page: #e8e9ec;
    --paper: #f4f4f5;
    --navy: #3a4a6c;
    --ink: #34466a;
    --muted: #9aa1ad;
    --rule: #b9bdc5;
    --white: #ffffff;
  }
  * { box-sizing: border-box; margin: 0; padding: 0; }
  html, body {
    width: 1200px; height: 720px; overflow: hidden;
    background: var(--page);
    font-family: "Poppins", sans-serif;
  }
  .stage {
    position: relative; width: 1200px; height: 720px;
    display: flex; align-items: center; justify-content: center; gap: 60px;
  }
  .card {
    position: relative; width: 520px; height: 320px;
    border-radius: 3px;
    box-shadow: 0 6px 18px rgba(40, 50, 70, 0.14);
  }
  .card-front { background: var(--paper); color: var(--ink); }
  .card-back { background: var(--navy); color: var(--white); }

  .wordmark {
    display: flex; align-items: center; gap: 12px;
    font-weight: 500; letter-spacing: 6px; white-space: nowrap;
  }
  .wordmark-dot { width: 14px; height: 14px; border-radius: 50%; background: currentColor; }

  .card-front .wordmark {
    position: absolute; left: 46px; top: 44px;
    font-size: 40px; color: var(--ink);
  }
  .front-rule { position: absolute; height: 1px; background: var(--rule); }
  .front-rule.upper { left: 46px; right: 46px; top: 118px; }
  .front-rule.lower { left: 46px; right: 46px; top: 232px; }

  .holder {
    position: absolute; left: 0; right: 0; top: 136px; text-align: center;
  }
  .holder-name { font-size: 22px; font-weight: 400; letter-spacing: 0.5px; color: var(--ink); }
  .holder-role { font-size: 11px; font-weight: 300; color: var(--muted); margin-top: 2px; }

  .contact-item {
    display: flex; align-items: flex-start; gap: 8px;
    font-size: 12px; line-height: 1.4; font-weight: 400; color: var(--ink);
    white-space: nowrap;
  }
  .contact-icon { width: 15px; height: 15px; flex: none; margin-top: 1px; }

  .contact-mail { position: absolute; right: 46px; top: 202px; }
  .contact-row {
    position: absolute; left: 46px; top: 250px;
    display: flex; gap: 48px; align-items: flex-start;
  }

  .card-back .wordmark {
    position: absolute; left: 50%; top: 50%;
    transform: translate(-50%, -50%);
    font-size: 52px; color: var(--white);
  }
  .web-address {
    position: absolute; left: 30px; bottom: 22px;
    font-size: 14px; font-weight: 500; letter-spacing: 0.5px; color: var(--white);
    white-space: nowrap;
  }
</style>
</head>
<body>
<main class="stage">
  <section class="card card-front" aria-label="Vorderseite">
    <div class="wordmark"><span class="wordmark-dot"></span>FORLAN</div>
    <div class="front-rule upper"></div>
    <div class="holder">
      <p class="holder-name">YOUR NAME</p>
      <p class="holder-role">Business card mockup</p>
    </div>
    <div class="contact-item contact-mail">
      <svg class="contact-icon" viewBox="0 0 16 16" aria-hidden="true">
        <rect x="1.5" y="3.5" width="13" height="9" rx="1" fill="none" stroke="currentColor" stroke-width="1.3"/>
        <path d="M2 4.2l6 4.6 6-4.6" fill="none" stroke="currentColor" stroke-width="1.3"/>
      </svg>
      <p>kontakt@forlan-beispiel.immo</p>
    </div>
    <div class="front-rule lower"></div>
    <div class="contact-row">
      <div class="contact-item">
        <svg class="contact-icon" viewBox="0 0 16 16" aria-hidden="true">
          <path d="M8 1.5a4.5 4.5 0 0 0-4.5 4.5c0 3.3 4.5 8.5 4.5 8.5s4.5-5.2 4.5-8.5A4.5 4.5 0 0 0 8 1.5z" fill="none" stroke="currentColor" stroke-width="1.4"/>
          <circle cx="8" cy="6" r="1.6" fill="currentColor"/>
        </svg>
        <p>Birkenauer Weg 21<br>12107 Berlin</p>
      </div>
      <div class="contact-item">
        <svg class="contact-icon" viewBox="0 0 16 16" aria-hidden="true">
          <path d="M4 2l2.2 2.6-1.3 1.6c.8 1.8 2.2 3.2 4 4l1.6-1.3L13 11l-1.2 2c-5 0-9.8-4.8-9.8-9.8z" fill="none" stroke="currentColor" stroke-width="1.3" stroke-linejoin="round"/>
        </svg>
        <p>+49 6251 4710562<br>+49 162 5074831</p>
      </div>
    </div>
  </section>

  <section class="card card-back" aria-label="Rückseite">
    <div class="wordmark"><span class="wordmark-dot"></span>FORLAN</div>
    <p class="web-address">www.forlan-beispiel.immo</p>
  </section>
</main>
</body>
</html>
```